Lend a Lantern Website Design (design layout only)

We need a website design for a new nonprofit organization based in Des Moines, Iowa called Lend a Lantern. The nonprofit provides soccer training opportunities to youth soccer players looking to improve their game while also affecting the lives of the less fortunate in a positive way. While participating in the training programs the players also go out and raise money for selected charities. The organization then donates the funds. In its first 18 months we donated $10,500. We would like to see designs attempt to symbolize the mission of the nonprofit - essentially "improve you while improving someone else."

We would like to see the following features:

· A place to donate - Our intent is to have the home page linked to the donation page; a simple straight-forward process for people to give money, and make donating as painless as possible - no account needed to make a donation, credit card or e-check should be the only information needed to donate, and have it be on a single page.

· A photo gallery so people can browse the photo gallery to get a better understanding of our organization and a place to add videos and a calendar to show upcoming events

· A place for contact information and the profiles of directors and board members. This should include a spot showing all the charities the organization donates to. Also includes a news section/blog for comments and suggestions.

We want the design to revolve around the content and mission. We would really like to stress our organization as nonprofit. We would also like if the website was user friendly and easy to navigate.

The logo of our organization is uploaded

```html
<!DOCTYPE html>
<html lang="en">
<head>
<meta charset="utf-8">
<title>Lend a Lantern</title>
<link href="https://fonts.googleapis.com/css2?family=Open+Sans:wght@400;600;700;800&display=swap" rel="stylesheet">
<style>
:root{
  --green:#3f8f2c;
  --green-light:#5fae3c;
  --dark:#1e1e1e;
  --nav:#2a2a2a;
  --text:#333;
  --muted:#666;
  --rule:#dcdcdc;
  --page:#ffffff;
  --bg:#f2f2f2;
}
*{box-sizing:border-box;margin:0;padding:0}
html,body{width:857px;height:1200px;overflow:hidden}
body{background:var(--bg);font-family:"Open Sans",Arial,sans-serif;color:var(--text);font-size:10px;line-height:1.45}
.page{position:relative;width:857px;height:1200px;background:var(--page)}
.header{position:absolute;left:57px;right:57px;top:0;height:128px}
.brand{position:absolute;left:0;top:58px;display:flex;align-items:center;gap:8px}
.brand-mark{width:26px;height:26px;background:var(--green)}
.brand-name{font-weight:800;font-size:22px;color:var(--green);letter-spacing:.5px;text-transform:uppercase;line-height:1}
.help{position:absolute;right:0;top:38px;font-size:13px;color:var(--green);font-weight:600}
.help span{color:var(--muted);font-weight:400}
.donate{position:absolute;right:0;top:66px;width:186px;height:38px;background:var(--dark);color:#fff;font-weight:700;font-size:18px;display:flex;align-items:center;justify-content:center;border-radius:3px}
.nav{position:absolute;left:57px;right:57px;top:128px;height:35px;background:var(--nav);display:flex}
.nav a{color:#ddd;text-decoration:none;font-size:9.5px;font-weight:600;text-transform:uppercase;padding:0 18px;display:flex;align-items:center}
.nav a.active{background:var(--green);color:#fff;padding:0 26px}
.hero{position:absolute;left:57px;right:57px;top:163px;height:289px;background:linear-gradient(180deg,#9fb7cf 0%,#b9c9b3 45%,#6f9a46 70%,#4f7d2f 100%)}
.arrow{position:absolute;top:130px;width:26px;height:30px;background:rgba(0,0,0,.7);display:flex;align-items:center;justify-content:center}
.arrow.left{left:0}.arrow.right{right:0}
.caption{position:absolute;left:20px;bottom:28px}
.caption h2{background:var(--green);color:#fff;font-size:20px;font-weight:700;padding:5px 12px;display:inline-block}
.caption p{background:rgba(0,0,0,.75);color:#fff;font-size:13px;padding:3px 12px;display:inline-block;margin-top:2px}
.main{position:absolute;left:57px;top:470px;width:510px}
.main h1{font-size:22px;font-weight:400;color:#222;margin-bottom:10px}
.main h3{font-size:17px;font-weight:400;color:var(--green);margin:18px 0 8px}
.main p{font-size:9.5px;color:var(--text);margin-bottom:10px}
.news{display:flex;gap:12px;margin-bottom:34px}
.news .thumb{flex:0 0 118px;height:80px;background:linear-gradient(135deg,#7aa353,#c6d8b4)}
.news p{margin:0}
.news b{color:var(--green)}
.sidebar{position:absolute;left:600px;top:470px;width:200px}
.sidebar h4{font-size:15px;font-weight:600;color:#222;padding-bottom:6px;border-bottom:2px solid var(--green);margin-bottom:8px}
.sidebar ul{list-style:none;margin-bottom:24px}
.sidebar li{font-size:9px;padding:4px 0 4px 12px;border-bottom:1px dotted var(--rule);position:relative}
.sidebar li::before{content:"";position:absolute;left:2px;top:9px;width:4px;height:4px;background:var(--green)}
.gallery-photo{height:88px;background:linear-gradient(180deg,#a9bfd2,#6e9a45)}
.footer{position:absolute;left:0;right:0;top:1043px;height:157px;background:var(--dark);color:#ccc}
.footer-inner{position:absolute;left:57px;right:57px;top:25px;display:flex;justify-content:space-between}
.contact{display:flex;gap:14px}
.contact h5{color:#fff;font-size:11px;font-weight:700;text-transform:uppercase}
.contact p{font-size:9px;color:#aaa}
.contact a{font-size:9px;color:var(--green-light);text-decoration:none}
.follow h5{color:#fff;font-size:12px;font-weight:600;text-align:center;margin-bottom:8px}
.socials{display:flex;gap:8px}
.socials span{width:22px;height:22px;border-radius:50%;background:#555}
.footer-brand{display:flex;align-items:center;gap:6px;font-weight:800;font-size:18px;color:var(--green);text-transform:uppercase}
.footer-brand i{width:20px;height:20px;background:var(--green);display:block}
.copyright{position:absolute;left:0;right:0;bottom:0;height:32px;border-top:1px solid #333;font-size:8.5px;color:#888;display:flex;align-items:center;justify-content:center}
</style>
</head>
<body>
<div class="page">
  <header class="header">
    <div class="brand"><span class="brand-mark"></span><span class="brand-name">Lend a Lantern</span></div>
    <div class="help">For Help Call <span>855.240.6618</span></div>
    <div class="donate">Donate Now</div>
  </header>
  <nav class="nav">
    <a class="active">Home</a><a>Who We Are</a><a>Training</a><a>Board of Directors</a><a>Board Members</a><a>Gallery</a><a>Contact</a>
  </nav>
  <section class="hero" role="img" aria-label="Photo of youth soccer players' legs around a ball on a grass pitch">
    <div class="arrow left"><svg width="10" height="12"><path d="M8 1 L2 6 L8 11" fill="none" stroke="#fff" stroke-width="2"/></svg></div>
    <div class="arrow right"><svg width="10" height="12"><path d="M2 1 L8 6 L2 11" fill="none" stroke="#fff" stroke-width="2"/></svg></div>
    <div class="caption"><h2>A Non Profit Orgnisation</h2><br><p>learn while helping Others</p></div>
  </section>
  <main class="main">
    <h1>WHAT WE DO</h1>
    <p>The nonprofit provides soccer training opportunities to youth soccer players looking to improve their game while also affecting the lives of the less fortunate in a positive way. While participating in the training programs the players also go out and raise money for selected charities. The organization then donates the funds. In its first 18 months we donated $10,500.</p>
    <h3>Our Mission</h3>
    <p>The nonprofit provides soccer training opportunities to youth soccer players looking to improve their game while also affecting the lives of the less fortunate in a positive way.</p>
    <p>While participating in the training programs the players also go out and raise money for selected charities. The organization then donates the funds. In its first 18 months we donated $10,500.</p>
    <h3>Latest News</h3>
    <div class="news">
      <div class="thumb" role="img" aria-label="Photo of young players at a training session"></div>
      <p>The nonprofit provides soccer training opportunities to youth soccer players looking to improve their game while also affecting the lives of the less fortunate in a positive way. While participating in the training programs the players also go out and raise money for selected charities. The organization then donates the funds. In its first 18 months we donated $10,500 ... <b>Read More...</b></p>
    </div>
    <div class="news">
      <div class="thumb" role="img" aria-label="Photo of a youth soccer match"></div>
      <p>The nonprofit provides soccer training opportunities to youth soccer players looking to improve their game while also affecting the lives of the less fortunate in a positive way. While participating in the training programs the players also go out and raise money for selected charities. The organization then donates the funds. In its first 18 months we donated $10,500 ... <b>Read More...</b></p>
    </div>
  </main>
  <aside class="sidebar">
    <h4>Upcoming Events</h4>
    <ul>
      <li>Robotic competitions teach students</li>
      <li>Robotic competitions teach students how to</li>
      <li>Robotic competitions teach</li>
      <li>Robotic competitions teach</li>
      <li>Robotic competitions teach students</li>
    </ul>
    <h4>Our Charities</h4>
    <ul>
      <li>In its first 18 months $10,500</li>
      <li>In its first 18 months we donated $10,500</li>
      <li>In its first 18 months $10,500</li>
      <li>In its first 18 months we donated</li>
      <li>In its first 18 months $10,500</li>
    </ul>
    <h4>Our Gallery</h4>
    <div class="gallery-photo" role="img" aria-label="Gallery photo of players competing for the ball"></div>
  </aside>
  <footer class="footer">
    <div class="footer-inner">
      <div class="contact">
        <svg width="22" height="30" viewBox="0 0 22 30"><path d="M11 0C5 0 0 5 0 11c0 8 11 19 11 19s11-11 11-19C22 5 17 0 11 0z" fill="#777"/><circle cx="11" cy="11" r="4" fill="#1e1e1e"/></svg>
        <div>
          <h5>Lend a Lantern</h5>
          <p>27 Birchway Lane,<br>Des Moines IA 50309</p>
          <a>Click Here to see the direction &gt;&gt;</a>
        </div>
      </div>
      <div class="follow">
        <h5>Follow Us On:</h5>
        <div class="socials"><span></span><span></span><span></span><span></span></div>
      </div>
      <div class="footer-brand"><i></i>Lend a Lantern</div>
    </div>
    <div class="copyright">Copyright © 2013 Lend a Lantern, All Rights Reserved.</div>
  </footer>
</div>
</body>
</html>
```